Brent Sowle Director / Photographer Branding

I need note pads, envelops, business cards and letter head for my company. I'm a fashion and advertising director / photographer. I'm having trouble deciding how to include both Director & Photographer in my title or if it is even necessary. Maybe just my name is enough. I'm open for even using my initials if it works with the design and overall pieces. Please view my website to see what I have at this moment and what work I do. www.brentsowle.example
Updates

Project Deadline Extended
Reason: Hello Everyone! I'm extending the deadline since I have been traveling on a job out of country and I wanted to have more time to look through all the designs and give enough time for everyone to provide changes with designs and updates. I will be more available to communicate online now that I'm back in the office! Thank you! Brent Sowle

Target Market(s)

Fashion magazines, clothing lines and beauty cosmetic brands.

Industry/Entity Type

Fashion Photography

Font styles to use
Sans Serif

Colors
acd036
acd35d
cbcbcb
f5f5f5

Requirements
Must have
• My name.. Brent Sowle, my website: brentsowle.example my phone number, 555-284-6031
• I don't need my address on these. I also live by the philosophy that less is more and keeping things simple ads strength to a design. I also don't want to stop people from taking chances and experimenting with an idea that might take me down different road with my branding.
Nice to have
• Bold designs and clean lines. I'm open to ideas that I could adopt but I lean towards a more minimalistic look in general.
Should not have
• Not have cheesy graphics or pictures. No images of cameras, film or anything that looks like it is a camera or aperture, lens etc... ;)

```html
<!DOCTYPE html>
<html lang="en">
<head>
<meta charset="utf-8">
<title>Brent Sowle — Business Cards</title>
<link href="https://fonts.googleapis.com/css2?family=Oswald:wght@400;700&display=swap" rel="stylesheet">
<style>
  :root {
    --backdrop: #62a5b6;
    --card: #f5f5f5;
    --deboss: #e9e9e9;
    --deboss-shade: #c4c4c4;
    --deboss-light: #ffffff;
    --dot: #e2e2e2;
    --dot-edge: #cbcbcb;
  }
  html, body {
    margin: 0;
    width: 1200px;
    height: 814px;
    overflow: hidden;
    background: var(--backdrop);
    font-family: "Oswald", sans-serif;
  }
  .stage {
    position: relative;
    width: 1200px;
    height: 814px;
  }
  .card {
    position: absolute;
    width: 520px;
    height: 297px;
    background: var(--card);
    box-shadow: 0 18px 40px rgba(20, 60, 75, 0.28);
  }
  .card--front { left: 620px; top: 120px; }
  .card--back { left: 70px; top: 400px; }

  .card__name {
    position: absolute;
    left: 40px;
    top: 30px;
    margin: 0;
    font-weight: 700;
    font-size: 50px;
    line-height: 0.92;
    letter-spacing: 1px;
    text-transform: uppercase;
    color: var(--deboss);
    text-shadow: 0 -1px 0 var(--deboss-shade), 0 1px 0 var(--deboss-light);
  }
  .card__braille {
    position: absolute;
    overflow: visible;
  }
  .card--front .card__braille { left: 232px; top: 42px; }
  .card--back .card__braille { left: 91px; top: 126px; }

  .braille-dot {
    fill: var(--dot);
    stroke: var(--dot-edge);
    stroke-width: 0.08;
  }

  .card__details {
    position: absolute;
    right: 36px;
    bottom: 30px;
    margin: 0;
    font-weight: 400;
    font-size: 13px;
    line-height: 1.45;
    text-align: right;
    color: var(--deboss);
    text-shadow: 0 -1px 0 var(--deboss-shade), 0 1px 0 var(--deboss-light);
  }
  .card__details span { display: block; }
</style>
</head>
<body>
<main class="stage">

  <svg width="0" height="0" style="position:absolute" aria-hidden="true">
    <defs>
      <g id="dot"><circle class="braille-dot" r="0.34"/></g>
      <g id="br-b"><use href="#dot" x="0" y="0"/><use href="#dot" x="0" y="1"/></g>
      <g id="br-r"><use href="#dot" x="0" y="0"/><use href="#dot" x="0" y="1"/><use href="#dot" x="0" y="2"/><use href="#dot" x="1" y="1"/></g>
      <g id="br-e"><use href="#dot" x="0" y="0"/><use href="#dot" x="1" y="1"/></g>
      <g id="br-n"><use href="#dot" x="0" y="0"/><use href="#dot" x="0" y="2"/><use href="#dot" x="1" y="0"/><use href="#dot" x="1" y="1"/></g>
      <g id="br-t"><use href="#dot" x="0" y="1"/><use href="#dot" x="0" y="2"/><use href="#dot" x="1" y="0"/><use href="#dot" x="1" y="1"/></g>
      <g id="br-s"><use href="#dot" x="0" y="1"/><use href="#dot" x="0" y="2"/><use href="#dot" x="1" y="0"/></g>
      <g id="br-o"><use href="#dot" x="0" y="0"/><use href="#dot" x="0" y="2"/><use href="#dot" x="1" y="1"/></g>
      <g id="br-w"><use href="#dot" x="0" y="1"/><use href="#dot" x="1" y="0"/><use href="#dot" x="1" y="1"/><use href="#dot" x="1" y="2"/></g>
      <g id="br-l"><use href="#dot" x="0" y="0"/><use href="#dot" x="0" y="1"/><use href="#dot" x="0" y="2"/></g>
    </defs>
  </svg>

  <section class="card card--front" aria-label="Business card front">
    <h1 class="card__name">Brent<br>Sowle</h1>
    <svg class="card__braille" width="240" height="110" aria-label="Brent Sowle in braille">
      <g transform="translate(4 4) scale(9.5)">
        <use href="#br-b" x="0"/><use href="#br-r" x="2.6"/><use href="#br-e" x="5.2"/><use href="#br-n" x="7.8"/><use href="#br-t" x="10.4"/>
        <g transform="translate(0 4.8)">
          <use href="#br-s" x="0"/><use href="#br-o" x="2.6"/><use href="#br-w" x="5.2"/><use href="#br-l" x="7.8"/><use href="#br-e" x="10.4"/>
        </g>
      </g>
    </svg>
    <p class="card__details">
      <span>Photographer / Director</span>
      <span>www.brentsowle.example</span>
      <span>555-284-6031</span>
    </p>
  </section>

  <section class="card card--back" aria-label="Business card back">
    <svg class="card__braille" width="350" height="40" aria-label="Brent Sowle in braille">
      <g transform="translate(4 4) scale(13)">
        <use href="#br-b" x="0"/><use href="#br-r" x="2.5"/><use href="#br-e" x="5"/><use href="#br-n" x="7.5"/><use href="#br-t" x="10"/>
        <use href="#br-s" x="15"/><use href="#br-o" x="17.5"/><use href="#br-w" x="20"/><use href="#br-l" x="22.5"/><use href="#br-e" x="25"/>
      </g>
    </svg>
  </section>

</main>
</body>
</html>
```